Label design - Superfood blend

We are a family owned nutrition company with big ambitions. Our goal is to develop a range of 100% natural supplements for women, inspired by nature & modern technology that helps them meet their nutritional needs while nourishing them from within. All our products are junk free because we believe that that’s how nature intended it. We also produce products through a sustainable process and only use biodegradable packaging for our products (See link - https://www.loamsack.org.uk/biodegradable-stand-pouch-250g-kraft)

Our brand style is modern and minimalist. This same style will be reflected in our social media, website and we want it to be represented through the label designs for our product packaging.

We want some creative designers to design a label that is true to our style (See attached packaging brief with designs we like) and displays our values of Premium, High Quality, Organic Real Food supplements focused on women. I have provided examples in the attached brief, but please only use as inspiration, I dont want any of them to be copied (sorry have had my fingers burnt already !)

Hello all, Please note this design is for a LABEL and not the whole package. We will have a 500gm biodegradable brown package, and we will have a label (which is what this project is about) that will be stuck on the front. The size of the label will be a rectangle (unless you come up with a new shape) in the size 20cm * 15cm. Please do not submit designs for the WHOLE from of the package, as we dont intend to have printed packages. Regards

Hello all, I have added a new logo version to the attachments, could you please also try that version. Could you also please look at the new sliders. We are only looking for a minimlaist theme. If you dont know what that means, please do feel free to ask, I would be happy to supply examples. Minimalist designs, means clean, modern, upmarket, elegant designs. It does not use too many colors and mostly sticks to a combination of black and white with colors used sparingly. See some below for your reference anyway. https://www.artvolley.co.uk/design/13359317 https://www.artvolley.co.uk/design/17270649 https://www.artvolley.co.uk/design/12584145 https://www.artvolley.co.uk/design/12367479 https://www.glimboard.com/search/pins/?q=minimalist%20label%20design&rs=rs&eq=&etslf=2809&term_meta[]=minimalist%7Crecentsearch%7Cundefined&term_meta[]=label%7Crecentsearch%7Cundefined&term_meta[]=design%7Crecentsearch%7Cundefined Regards

Target Market(s)

The target market is women between the age 25 to 45, based in UK (mostly based in larger cities in UK). They are typically middle class or higher and would be in demanding jobs and social lives, that requires for them to meet their nutrition needs in convenient, easy to take forms. The women would also be socially conscious and sensitive to issues like women's rights, environmental issues, healthy food, organic food and sustainability etc. I have a much more detailed customer avatar if required

Font styles to use
Serif
Sans Serif
Decorative
Script

Colors
e8e8e8
474747
1b1b1b
add136

Requirements
Must have
• The label, should look minimalist and modern, throw in some out of the box creativity and we have a winner. Creativity will definitely be of importance. Our packaging is a biodegradable brown paper stand up pouch (Example link in product description). So to make it standout from other colorful packaging - being creative would definitely help.
• Please use the color schemes provided in the brief (See attachments). But if you want to experiment I would be open to it, as long as they are still minimalist and does not stray very far from the color given in the brief :)

```html
<!DOCTYPE html>
<html lang="en">
<head>
<meta charset="utf-8">
<title>Veraline – Tend Thy Gut labels</title>
<link rel="stylesheet" href="https://fonts.googleapis.com/css2?family=Montserrat:wght@300;400;500;600;700;800&display=swap">
<style>
  :root {
    --canvas: #e7e8e9;
    --label: #ffffff;
    --ink: #111111;
    --rule: #4a4a4a;
    --green: #79c99b;
    --badge: #cfcfcf;
  }
  * { box-sizing: border-box; margin: 0; padding: 0; }
  html, body { width: 1200px; height: 1200px; overflow: hidden; }
  body {
    background: var(--canvas);
    font-family: "Montserrat", Arial, sans-serif;
    color: var(--ink);
    position: relative;
  }
  .label {
    position: absolute;
    width: 365px;
    height: 486px;
    background: var(--label);
    border-radius: 13px;
    overflow: hidden;
    transform-origin: 0 0;
  }
  .label--500 { left: 235px; top: 357px; }
  .label--300 { left: 706px; top: 478px; transform: scale(0.74); }

  .brand {
    position: absolute;
    left: -145px;
    top: 196px;
    width: 394px;
    height: 44px;
    transform: rotate(-90deg);
    display: flex;
    justify-content: space-between;
    align-items: center;
    font-size: 48px;
    font-weight: 500;
    line-height: 1;
    color: var(--ink);
  }

  .product-name {
    position: absolute;
    left: 112px;
    top: 128px;
    line-height: 1;
  }
  .product-name__main {
    display: block;
    font-size: 72px;
    font-weight: 700;
    letter-spacing: -2px;
  }
  .product-name__sub {
    display: block;
    margin-top: 4px;
    margin-left: 5px;
    font-size: 45px;
    font-weight: 700;
    color: var(--green);
  }

  .tagline {
    position: absolute;
    left: 112px;
    top: 256px;
    width: 219px;
    border-top: 1px solid var(--rule);
    padding-top: 6px;
    font-size: 9.3px;
    font-weight: 600;
    letter-spacing: -0.3px;
    white-space: nowrap;
  }

  .ingredients {
    position: absolute;
    left: 112px;
    top: 300px;
    width: 198px;
    list-style: none;
  }
  .ingredients li {
    display: flex;
    align-items: center;
    height: 22.5px;
    border-bottom: 1px solid var(--rule);
    font-size: 12.8px;
    font-weight: 300;
    white-space: nowrap;
  }
  .ingredients .divider {
    display: inline-block;
    width: 1px;
    height: 15px;
    background: var(--ink);
    margin: 0 15px 0 13px;
  }

  .category {
    position: absolute;
    left: 112px;
    top: 404px;
    font-size: 11px;
    font-weight: 700;
  }

  .footer {
    position: absolute;
    left: 0;
    right: 0;
    top: 431px;
    bottom: 0;
    border-top: 1px solid var(--rule);
  }
  .net-weight {
    position: absolute;
    left: 20px;
    top: 13px;
    width: 66px;
    text-align: center;
    font-size: 11px;
    font-weight: 400;
    line-height: 15px;
  }
  .badges {
    position: absolute;
    right: 36px;
    top: 8px;
    display: flex;
    gap: 14px;
  }
  .badge { width: 37px; height: 37px; }
</style>
</head>
<body>

<div class="label label--500">
  <div class="brand"><span>V</span><span>E</span><span>R</span><span>A</span><span>L</span><span>I</span><span>N</span><span>E</span></div>
  <h1 class="product-name"><span class="product-name__main">TEND</span><span class="product-name__sub">THY GUT</span></h1>
  <p class="tagline">Organic Prebiotics And Superfood Blend For Women</p>
  <ul class="ingredients">
    <li>Baobab<span class="divider"></span>Flaxseed</li>
    <li>Acai Berry<span class="divider"></span>Maca Powder</li>
    <li>Goji Berry<span class="divider"></span>Aronia Berry</li>
    <li>Camu Camu<span class="divider"></span>Cinnamon</li>
  </ul>
  <p class="category">FOOD SUPPLEMENT</p>
  <div class="footer">
    <p class="net-weight">Net Weight<br>500 gm</p>
    <div class="badges">
      <svg class="badge" viewBox="0 0 40 40" role="img" aria-label="Organic certification badge"><circle cx="20" cy="20" r="18" fill="none" stroke="#333" stroke-width="1.5"/></svg>
      <svg class="badge" viewBox="0 0 40 40" role="img" aria-label="Vegan certification badge"><circle cx="20" cy="20" r="18" fill="none" stroke="#333" stroke-width="1.5"/></svg>
    </div>
  </div>
</div>

<div class="label label--300">
  <div class="brand"><span>V</span><span>E</span><span>R</span><span>A</span><span>L</span><span>I</span><span>N</span><span>E</span></div>
  <h2 class="product-name"><span class="product-name__main">TEND</span><span class="product-name__sub">THY GUT</span></h2>
  <p class="tagline">Organic Prebiotics And Superfood Blend For Women</p>
  <ul class="ingredients">
    <li>Baobab<span class="divider"></span>Flaxseed</li>
    <li>Acai Berry<span class="divider"></span>Maca Powder</li>
    <li>Goji Berry<span class="divider"></span>Aronia Berry</li>
    <li>Camu Camu<span class="divider"></span>Cinnamon</li>
  </ul>
  <p class="category">FOOD SUPPLEMENT</p>
  <div class="footer">
    <p class="net-weight">Net Weight<br>300 gm</p>
    <div class="badges">
      <svg class="badge" viewBox="0 0 40 40" role="img" aria-label="Organic certification badge"><circle cx="20" cy="20" r="18" fill="none" stroke="#333" stroke-width="1.5"/></svg>
      <svg class="badge" viewBox="0 0 40 40" role="img" aria-label="Vegan certification badge"><circle cx="20" cy="20" r="18" fill="none" stroke="#333" stroke-width="1.5"/></svg>
    </div>
  </div>
</div>

</body>
</html>
```